Postcard design for accounting company

We need a postcard design (front and back) to our accounting firm that provides bookkeeping services to small and mid-size companies using LedgerPad Online. We would like to see designs that use the color blue and match our overall branding (see website). The final design should communicate professionalism, trust, and ease.

Target Market(s)

Small and Mid-Size companies

Industry/Entity Type

Accounting

Colors
0054AA
0677BA
7BADD7
CADEEF
E8F1F8

Requirements
Must have
• Logo, contact information, indicate services offered, color blue, and fit postcard template (see attached). Contact info = 555.318.2207, 1.800.555.0142, Info@BrightLedgerAccounting.com, www.BrightLedgerAccounting.com. Use the ZRPX Retail Indicia, which is a postage payment mark that takes the place of a regular postage stamp or meter stamp. Every ZRPX mailpiece must include the ZRPX Retail Indicia above and to the right of the address block. The ZRPX Retail Indicia does not have a specific size requirement but must be larger than 0.5" x 0.5". The type font must be in all caps and at least a 4 point size. It should fit in the area 1.625" from the right edge and 1.375" from top edge. Leave 1/8" of space around the top and right edge. See attached sample.
Nice to have
• Include that we a re Certified LedgerPad CertPartners (can include LPO logo). Also, maybe include the logos of the associations we are members of (North Pinecrest Chamber of Commerce, Federal Guild of Certified Ledgerkeepers, and Continental League of Female Enterprise Founders.

```html
<!DOCTYPE html>
<html lang="en">
<head>
<meta charset="utf-8">
<title>Bright Ledger Accounting – Postcard Front and Back</title>
<link rel="stylesheet" href="https://fonts.googleapis.com/css2?family=Fira+Sans:wght@500;600;700&family=Fira+Sans+Condensed:wght@600;700;800&family=Lato:wght@400;700&family=Libre+Baskerville&display=swap">
<style>
  :root {
    --page-bg: #a6a6a6;
    --navy: #1d3e78;
    --navy-deep: #1f3b70;
    --blue-top: #0f6aae;
    --blue-bottom: #1d4585;
    --brand-blue: #0054aa;
    --mid-blue: #0677ba;
    --cyan: #1ea3c9;
    --cyan-line: #37b6dc;
    --arrow-blue: #1a5fa6;
    --soft-blue: #7badd7;
    --pale-blue: #cadeef;
    --ice: #e8f1f8;
    --white: #ffffff;
    --rule: #c9ced4;
    --ink: #1e2f55;
  }
  * { margin: 0; padding: 0; box-sizing: border-box; }
  html, body { width: 1200px; height: 904px; overflow: hidden; }
  body { background: var(--page-bg); position: relative; font-family: "Fira Sans", sans-serif; }

  .postcard {
    position: absolute;
    width: 533px;
    height: 359px;
    background: var(--white);
    overflow: hidden;
    box-shadow: 0 4px 12px rgba(0,0,0,0.18);
  }
  .postcard--front { left: 148px; top: 74px; }
  .postcard--back { left: 535px; top: 471px; }
  .postcard__art { position: absolute; inset: 0; width: 533px; height: 359px; }
  .postcard__text { position: absolute; white-space: nowrap; }

  /* ---------- front ---------- */
  .brand-name {
    position: absolute;
    font-family: "Libre Baskerville", serif;
    font-weight: 400;
    color: var(--navy);
  }
  .postcard--front .brand-name { left: 22px; top: 16px; width: 180px; font-size: 21px; line-height: 25px; }
  .front-title {
    left: 21px; top: 119px;
    font-family: "Fira Sans Condensed", sans-serif; font-weight: 700;
    font-size: 37px; line-height: 37px; color: var(--white); letter-spacing: 0.5px;
  }
  .front-subtitle {
    left: 21px; top: 161px;
    font-family: "Fira Sans Condensed", sans-serif; font-weight: 700;
    font-size: 23px; line-height: 23px; color: var(--white);
  }
  .front-tagline {
    left: 71px; top: 203px;
    font-size: 11.5px; line-height: 14.5px; font-weight: 500; color: var(--white);
  }
  .front-cta {
    left: 21px; top: 268px;
    font-family: "Fira Sans Condensed", sans-serif; font-weight: 800;
    font-size: 15px; line-height: 18px; color: var(--navy);
  }
  .contact-line { font-family: "Lato", sans-serif; color: var(--white); }
  .postcard--front .contact-line { left: 37px; font-size: 11px; line-height: 14px; }
  .front-phone { top: 319px; }
  .front-email { top: 337px; }
  .front-web {
    left: 300px; top: 333px; width: 236px; text-align: center;
    font-size: 12px; line-height: 14px; font-weight: 500; color: var(--white);
  }

  /* ---------- back ---------- */
  .postcard--back .brand-name { left: 342px; top: 20px; width: 110px; font-size: 13.5px; line-height: 16px; }
  .indicia {
    position: absolute; left: 468px; top: 22px; width: 43px; height: 43px;
    border: 0.8px solid var(--rule);
    display: flex; flex-direction: column; justify-content: center; align-items: center;
    font-family: "Lato", sans-serif; font-weight: 700; font-size: 5.2px; line-height: 7px;
    color: #222; text-transform: uppercase; text-align: center;
  }
  .address-rule { position: absolute; height: 1px; background: var(--rule); }

  .services-label {
    left: 21px; top: 18px;
    font-family: "Fira Sans Condensed", sans-serif; font-weight: 800;
    font-size: 13px; line-height: 17px; color: var(--white);
  }
  .service-heading {
    left: 76px;
    font-family: "Fira Sans", sans-serif; font-weight: 600;
    font-size: 12.5px; line-height: 14px; color: var(--white);
  }
  .service-line {
    font-family: "Lato", sans-serif; font-size: 8.8px; line-height: 11px;
    color: var(--white); text-align: justify; text-align-last: justify;
  }
  .service-line--end { text-align-last: left; }
  .proadvisor-note {
    left: 21px; top: 295px;
    font-family: "Fira Sans", sans-serif; font-weight: 600;
    font-size: 9.8px; line-height: 12.3px; color: var(--ink);
  }
  .postcard--back .contact-line { left: 310px; font-size: 11.5px; line-height: 14px; }
</style>
</head>
<body>

<!-- FRONT -->
<section class="postcard postcard--front" aria-label="Postcard front">
  <svg class="postcard__art" viewBox="0 0 533 359" aria-hidden="false">
    <defs>
      <linearGradient id="photoTone" x1="0" y1="0" x2="1" y2="1">
        <stop offset="0" stop-color="#d7dde4"/>
        <stop offset="0.55" stop-color="#c3ccd7"/>
        <stop offset="1" stop-color="#a9b5c4"/>
      </linearGradient>
      <linearGradient id="domeBlue" x1="0" y1="0" x2="0" y2="1">
        <stop offset="0" stop-color="#0f6aae"/>
        <stop offset="1" stop-color="#1d4585"/>
      </linearGradient>
    </defs>
    <path role="img" aria-label="Photo of a hand with a pen using a calculator beside a laptop showing an accounting dashboard"
          d="M215,0 C205,30 200,60 200,95 L200,359 L533,359 L533,0 Z" fill="url(#photoTone)"/>
    <path class="accent-band" d="M288,359 C380,320 470,280 533,226 L533,359 Z" fill="var(--cyan)"/>
    <path class="panel-white" d="M0,140 C40,108 95,92 150,92 C235,92 300,165 304,259 C306,290 300,330 285,359 L0,359 Z" fill="var(--white)"/>
    <path class="panel-blue" d="M0,140 C40,108 95,92 150,92 C235,92 300,165 304,259 L0,259 Z" fill="url(#domeBlue)"/>
    <path class="panel-navy" d="M0,313 L298,313 C294,330 290,345 283,359 L0,359 Z" fill="var(--navy-deep)"/>
    <path class="growth-arrow" d="M292,359 C318,300 318,205 258,152" fill="none" stroke="var(--arrow-blue)" stroke-width="3"/>
    <polygon points="241,133 252,167 271,146" fill="var(--white)" stroke="var(--arrow-blue)" stroke-width="2"/>
    <circle class="feature-dot" cx="42" cy="223" r="20" fill="var(--soft-blue)"/>
    <circle class="member-badge" cx="177" cy="286" r="18" fill="#c9d4c0"/>
    <circle class="member-badge" cx="224" cy="286" r="18" fill="#cfe0dc"/>
    <circle class="member-badge" cx="269" cy="286" r="18" fill="#e9dcc0"/>
    <g class="icon-phone" transform="translate(20,321)" fill="none" stroke="var(--cyan-line)" stroke-width="1.4">
      <path d="M2,1 L4.5,1 L5.5,3.5 L4,4.8 C4.8,6.6 6,7.8 7.6,8.6 L8.8,7.1 L11,8.2 L11,10.5 C6,10.8 1.5,6.2 2,1 Z"/>
    </g>
    <g class="icon-mail" transform="translate(20,340)" fill="none" stroke="var(--cyan-line)" stroke-width="1.3">
      <rect x="0.5" y="1.5" width="11" height="7.5"/>
      <path d="M0.5,1.5 L6,6 L11.5,1.5"/>
    </g>
  </svg>

  <div class="brand-name">Bright Ledger Accounting</div>
  <div class="postcard__text front-title">ACCOUNTING</div>
  <div class="postcard__text front-subtitle">FOR YOUR BUSINESS</div>
  <div class="postcard__text front-tagline">Specializing in Cloud-Based<br>Bookkeeping &amp; Payroll Processing<br>with LedgerPad Online by Tallywise.</div>
  <div class="postcard__text front-cta">REQUEST A FREE<br>QUOTE TODAY!</div>
  <div class="postcard__text contact-line front-phone">555.318.2207 / 1.800.555.0142</div>
  <div class="postcard__text contact-line front-email">info@brightledgeraccounting.com</div>
  <div class="postcard__text front-web">www.brightledgeraccounting.com</div>
</section>

<!-- BACK -->
<section class="postcard postcard--back" aria-label="Postcard back">
  <svg class="postcard__art" viewBox="0 0 533 359">
    <defs>
      <linearGradient id="serviceBlue" x1="0.8" y1="0" x2="0.2" y2="1">
        <stop offset="0" stop-color="#0f62a6"/>
        <stop offset="1" stop-color="#1e4a88"/>
      </linearGradient>
    </defs>
    <path class="band-contact" d="M265,292 L533,292 L533,359 L278,359 C275,335 270,312 265,292 Z" fill="#15589c"/>
    <path class="panel-services" d="M0,0 L276,0 C314,45 330,105 327,155 C324,210 302,262 270,300 L0,300 Z" fill="url(#serviceBlue)"/>
    <path class="panel-note" d="M0,296 C60,282 110,272 160,272 C200,272 235,285 270,300 L278,359 L0,359 Z" fill="var(--white)"/>
    <path class="growth-arrow" d="M282,359 C305,318 338,250 336,160 C334,100 320,62 301,34" fill="none" stroke="var(--arrow-blue)" stroke-width="3"/>
    <polygon points="288,19 295,45 320,36" fill="var(--white)" stroke="var(--arrow-blue)" stroke-width="2"/>
    <polygon class="services-tab" points="0,17 132,17 125,36 0,36" fill="var(--cyan)"/>

    <g class="service-icon" fill="none" stroke="var(--cyan-line)" stroke-width="1.4">
      <circle cx="43" cy="66" r="21" fill="#1a64a6"/>
      <rect x="35" y="55" width="13" height="18" rx="1"/>
      <path d="M38,60 H45 M38,64 H45 M38,68 H43"/>
      <rect x="44" y="64" width="9" height="11" rx="1"/>
      <circle cx="43" cy="149" r="21" fill="#1a60a2"/>
      <rect x="35" y="138" width="16" height="20" rx="1"/>
      <path d="M38,155 V150 M42,155 V146 M46,155 V148"/>
      <circle cx="50" cy="156" r="4"/>
      <circle cx="43" cy="221" r="21" fill="#1b5c9c"/>
      <rect x="40" y="209" width="12" height="19" rx="2"/>
      <circle cx="38" cy="219" r="5"/>
      <path d="M34.5,222.5 L30,227"/>
    </g>

    <rect class="partner-badge" x="198" y="273" width="55" height="75" fill="var(--white)" stroke="#dde3ea" stroke-width="1"/>
    <rect x="198" y="330" width="55" height="10" fill="#6cc04a"/>

    <line class="address-rule-line" x1="350" y1="152" x2="511" y2="152" stroke="var(--rule)" stroke-width="1"/>
    <line x1="343" y1="189" x2="511" y2="189" stroke="var(--rule)" stroke-width="1"/>
    <line x1="339" y1="225" x2="511" y2="225" stroke="var(--rule)" stroke-width="1"/>

    <g class="icon-phone" transform="translate(292,302)" fill="none" stroke="var(--cyan-line)" stroke-width="1.4">
      <path d="M2,1 L4.5,1 L5.5,3.5 L4,4.8 C4.8,6.6 6,7.8 7.6,8.6 L8.8,7.1 L11,8.2 L11,10.5 C6,10.8 1.5,6.2 2,1 Z"/>
    </g>
    <g class="icon-mail" transform="translate(292,321)" fill="none" stroke="var(--cyan-line)" stroke-width="1.3">
      <rect x="0.5" y="1.5" width="11" height="7.5"/>
      <path d="M0.5,1.5 L6,6 L11.5,1.5"/>
    </g>
    <g class="icon-globe" transform="translate(292,338)" fill="none" stroke="var(--cyan-line)" stroke-width="1.1">
      <circle cx="6" cy="6" r="5.2"/>
      <ellipse cx="6" cy="6" rx="2.3" ry="5.2"/>
      <path d="M0.8,6 H11.2"/>
    </g>
  </svg>

  <div class="brand-name">Bright Ledger Accounting</div>
  <div class="indicia"><span>PRSRT STD</span><span>ECRWSS</span><span>U.S.POSTAGE</span><span>PAID</span><span>ZRPX Retail</span></div>

  <div class="postcard__text services-label">OUR SERVICES:</div>

  <div class="postcard__text service-heading" style="top:45px">BOOKKEEPING</div>
  <div class="postcard__text service-line" style="left:76px;top:58px;width:221px">Let us take over the day to day bookkeeping so you</div>
  <div class="postcard__text service-line" style="left:76px;top:70px;width:221px">can get back to running your business. We offer</div>
  <div class="postcard__text service-line" style="left:70px;top:81px;width:227px">LedgerPad Online setup and ongoing bookkeeping,</div>
  <div class="postcard__text service-line" style="left:21px;top:93px;width:277px">including daily journal entries, accounts payables &amp; receivables, bill</div>
  <div class="postcard__text service-line" style="left:21px;top:105px;width:282px">pay, sales tax reporting &amp; payments, account reconciliation, and more.</div>

  <div class="postcard__text service-heading" style="top:128px">FINANCIAL REPORTING</div>
  <div class="postcard__text service-line" style="left:76px;top:142px;width:231px">We'll provide easy to understand financial reports that</div>
  <div class="postcard__text service-line" style="left:76px;top:154px;width:231px">allow you &amp; your team to manage cash flow, create</div>
  <div class="postcard__text service-line" style="left:70px;top:165px;width:237px">budgets &amp; make forecasting decisions. Want real time data?</div>
  <div class="postcard__text service-line" style="left:21px;top:177px;width:278px">Let us provide solutions with the latest in mobile apps &amp; dashboards.</div>

  <div class="postcard__text service-heading" style="top:200px">PAYROLL PROCESSING</div>
  <div class="postcard__text service-line" style="left:76px;top:213px;width:219px">Whether you have 5 employees or 100+, payroll can be</div>
  <div class="postcard__text service-line" style="left:76px;top:225px;width:215px">an overwhelming and time consuming task. We offer</div>
  <div class="postcard__text service-line" style="left:70px;top:237px;width:221px">full service payroll processing, including employee</div>
  <div class="postcard__text service-line service-line--end" style="left:21px;top:248px;width:200px">onboarding and reporting.</div>

  <div class="postcard__text proadvisor-note">Our Certified LedgerPad<br>CertPartners have the Knowledge<br>and Expertise to Ensure Professional,<br>Accurate, High Quality Service.</div>

  <div class="postcard__text contact-line" style="top:301px">555.318.2207 / 1.800.555.0142</div>
  <div class="postcard__text contact-line" style="top:320px">info@brightledgeraccounting.com</div>
  <div class="postcard__text contact-line" style="top:337px">www.brightledgeraccounting.com</div>
</section>

</body>
</html>
```